Website for Torvane Capital - investment banking firm

We have a corporate identity (thanks to Ravella/48213) and want to extend that into a website design.  See the attached zipped files.
We have software folks in-house to do the coding.
See the attached Project Brief & Notes for more details.  Don't worry about the actual text - lorem ipsum will be fine.
The server will be Apache.
Thank you!
Leopold

```html
<!DOCTYPE html>
<html lang="en">
<head>
<meta charset="utf-8">
<title>Torvane Capital</title>
<link rel="stylesheet" href="https://fonts.googleapis.com/css2?family=Open+Sans:ital,wght@0,400;0,600;0,700;1,700&family=Raleway:wght@400;500&display=swap">
<style>
:root{
  --brand:#22509f;
  --brand-dark:#1a4589;
  --heading:#1d4f86;
  --link:#2b5c9f;
  --tab:#3c6e8e;
  --tab-fold:#274d66;
  --ink:#333;
  --muted:#555;
  --accent:#9a2b3c;
  --social:#9a9a9a;
  --rule:#cfcfcf;
}
*{box-sizing:border-box;margin:0;padding:0}
html,body{width:1200px;height:1055px;overflow:hidden}
body{position:relative;background:#fff;font-family:"Open Sans",Arial,sans-serif;color:var(--ink)}
.abs{position:absolute}

.brand{left:130px;top:40px;display:flex;align-items:center;gap:14px}
.brand-mark{width:62px;height:62px;border:4px solid var(--brand);border-radius:50%}
.brand-name{font-size:36px;font-weight:600;color:var(--brand);letter-spacing:.5px}

.online-banking{left:900px;top:58px;width:169px;height:34px;background:#000;border:1px solid #444;color:#fff;font-size:13px;font-weight:600;display:flex;align-items:center;padding-left:12px;gap:10px}

.main-nav{left:130px;top:138px;width:939px;height:48px;background:var(--brand);border-radius:4px;display:flex;align-items:center}
.main-nav .home{margin-left:17px;margin-right:4px}
.main-nav a{color:#fff;text-decoration:none;font-size:15px;font-weight:600;padding:0 15px;border-left:1px solid rgba(255,255,255,.18)}
.main-nav a:first-of-type{border-left:1px solid rgba(255,255,255,.18);margin-left:12px}
.search{left:812px;top:151px;width:242px;height:24px;background:#fff;border-radius:2px}
.search-btn{right:0;top:0;width:26px;height:24px;background:#9a9a9a;border-radius:0 2px 2px 0;display:flex;align-items:center;justify-content:center}

.hero-photo{left:130px;top:195px;width:417px;height:323px;background:linear-gradient(135deg,#5a4410 0%,#d9b23c 30%,#fff1a8 45%,#b88a1e 62%,#f2d46a 78%,#6b5210 100%)}
.hero-panel{left:547px;top:195px;width:522px;height:323px;background:linear-gradient(180deg,#2156a6,#1c4c95)}
.hero-title{left:590px;top:230px;font-family:"Raleway",sans-serif;font-size:44px;font-weight:500;color:#fff;line-height:51px}
.hero-text{left:591px;top:345px;font-size:20px;color:#fff;line-height:26px}
.hero-btn{left:592px;top:415px;width:148px;height:35px;background:#8c8c8c;color:#fff;font-size:17px;font-weight:700;display:flex;align-items:center;padding-left:10px;gap:10px}

.slider-dots{left:573px;top:525px;display:flex;gap:4px}
.slider-dots span{width:11px;height:11px;border-radius:3px;background:#1c4a8a}
.slider-dots span.active{background:#9a9ab0}

.backdrop{left:0;top:540px;width:1200px;height:300px;background:radial-gradient(ellipse at center,#f3f3f3 0%,#fff 70%)}
.card{background:#fff;border-radius:6px;box-shadow:0 3px 10px rgba(0,0,0,.14)}
.welcome-card{left:130px;top:548px;width:580px;height:247px}
.presence-card{left:755px;top:548px;width:320px;height:247px}
.tab{height:35px;background:var(--tab);color:#fff;font-style:italic;font-weight:700;font-size:21px;display:flex;align-items:center;gap:6px;padding-left:10px}
.tab::after{content:"";position:absolute;left:0;top:35px;border-top:10px solid var(--tab-fold);border-left:10px solid transparent}
.welcome-tab{left:120px;top:545px;width:141px}
.presence-tab{left:745px;top:545px;width:182px}

.welcome-title{left:139px;top:604px;font-size:20px;font-weight:600;color:var(--heading)}
.points{left:141px;top:654px;width:520px;list-style:none}
.points li{position:relative;padding-left:20px;font-size:12px;line-height:18px;color:var(--ink);margin-bottom:16px}
.points li b{font-weight:400;color:#111}
.points li svg{position:absolute;left:0;top:4px}

.map{left:778px;top:600px;width:272px;height:172px;border:2px solid #e4e4e4;background:linear-gradient(135deg,#e6e2da,#d8d4cc 50%,#e9e5de)}

.footer-links{top:851px;list-style:none}
.footer-links li{font-size:13px;line-height:30px;color:var(--link)}
.footer-icons{left:855px;top:857px;display:flex;flex-direction:column;gap:12px}

.rule{left:127px;top:955px;width:1073px;height:1px;background:var(--rule)}
.foot-brand{left:134px;top:980px;display:flex;align-items:center;gap:8px}
.foot-brand .brand-mark{width:26px;height:26px;border-width:2px}
.foot-brand .brand-name{font-size:16px}
.copyright{left:313px;top:983px;font-size:13px;color:var(--muted)}
.social{left:896px;top:978px;display:flex;gap:5px}
.social span{width:30px;height:30px;border-radius:50%;background:var(--social)}
</style>
</head>
<body>
<div class="abs brand"><span class="brand-mark"></span><span class="brand-name">Torvane Capital</span></div>
<div class="abs online-banking"><svg width="8" height="10" viewBox="0 0 8 10"><path d="M2 1l4 4-4 4" stroke="#fff" stroke-width="1.6" fill="none"/></svg>Online Banking</div>

<nav class="abs main-nav">
  <svg class="home" width="22" height="20" viewBox="0 0 22 20"><path d="M11 1L1 10h3v9h5v-6h4v6h5v-9h3z" fill="#fff"/></svg>
  <a>About</a><a>Services</a><a>Current Engagements</a><a>Completed Transactions</a>
</nav>
<div class="abs search"><div class="abs search-btn"><svg width="12" height="12" viewBox="0 0 12 12"><circle cx="5" cy="5" r="3.5" stroke="#fff" stroke-width="1.6" fill="none"/><path d="M7.5 7.5L11 11" stroke="#fff" stroke-width="1.8"/></svg></div></div>

<div class="abs hero-photo" role="img" aria-label="Photograph of stacked gold bullion bars"></div>
<div class="abs hero-panel"></div>
<h1 class="abs hero-title" style="font-weight:500">Trusted or Disciplined<br>Effective?</h1>
<p class="abs hero-text">Torvane Capital is an independent<br>investment bank working for</p>
<div class="abs hero-btn">Learn More <svg width="10" height="14" viewBox="0 0 10 14"><path d="M2 1l6 6-6 6" stroke="#fff" stroke-width="2.4" fill="none"/></svg></div>
<div class="abs slider-dots"><span></span><span></span><span class="active"></span><span></span></div>

<div class="abs backdrop"></div>
<section class="abs card welcome-card"></section>
<section class="abs card presence-card"></section>
<div class="abs tab welcome-tab"><svg width="24" height="22" viewBox="0 0 24 22"><path d="M2 8h5l10-6v18L7 14H2z" fill="#fff"/><path d="M5 14l2 7h3l-2-7" fill="#fff"/></svg>Welcome</div>
<div class="abs tab presence-tab"><svg width="16" height="24" viewBox="0 0 16 24"><path d="M8 1a7 7 0 0 0-7 7c0 6 7 15 7 15s7-9 7-15a7 7 0 0 0-7-7z" fill="#fff"/><circle cx="8" cy="8" r="2.5" fill="#3c6e8e"/></svg>Our Presence</div>

<h2 class="abs welcome-title">Global Investment Banking Services</h2>
<ul class="abs points">
  <li><svg width="12" height="10" viewBox="0 0 12 10"><path d="M0 5h10M6 1l4 4-4 4" stroke="#1d4f86" stroke-width="1.6" fill="none"/></svg><b>Lorem ipsum dolor sit amet</b> - Consectetur adipiscing elit. Sed sagittis consectetur nunc in blandit. Donec aliquam, lacus vel semper congue, sem tellus tincidunt turpisns.</li>
  <li><svg width="12" height="10" viewBox="0 0 12 10"><path d="M0 5h10M6 1l4 4-4 4" stroke="#1d4f86" stroke-width="1.6" fill="none"/></svg><b>Lorem ipsum dolor sit amet</b> - Consectetur adipiscing elit. Sed sagittis consectetur nunc in blandit. Donec aliquam, lacus vel semper congue, sem tellusenim.</li>
</ul>
<div class="abs map" role="img" aria-label="Street map showing office locations with pins"></div>

<ul class="abs footer-links" style="left:131px"><li>VIP Enhanced Online Security</li><li>Sitemap</li><li>Lost or stolen cards</li></ul>
<ul class="abs footer-links" style="left:375px"><li>Disclosure documents</li><li>Dispute resolution</li><li>Find a branch</li></ul>
<ul class="abs footer-links" style="left:577px"><li>VIP Enhanced Online Security</li><li>Sitemap</li><li>Lost or stolen cards</li></ul>
<div class="abs footer-icons">
  <svg width="18" height="18" viewBox="0 0 18 18"><path d="M16 16L3 3M3 3v8M3 3h8" stroke="#9a2b3c" stroke-width="3" fill="none"/></svg>
  <svg width="18" height="18" viewBox="0 0 18 18"><rect x="5" y="0" width="9" height="18" rx="1.5" fill="#9a2b3c"/><rect x="6.5" y="2" width="6" height="8" fill="#fff"/></svg>
  <svg width="18" height="18" viewBox="0 0 18 18"><circle cx="9" cy="5" r="4.5" fill="#9a2b3c"/><path d="M1 18c0-6 16-6 16 0z" fill="#9a2b3c"/></svg>
</div>
<ul class="abs footer-links" style="left:897px"><li>VIP Enhanced Online Security</li><li>Sitemap</li><li>Lost or stolen cards</li></ul>

<div class="abs rule"></div>
<div class="abs foot-brand"><span class="brand-mark"></span><span class="brand-name">Torvane Capital</span></div>
<p class="abs copyright">Copyright Torvane ABN 41 562 908 137 AFSL/japan Credit Licence 518204</p>
<div class="abs social" aria-label="Social links"><span></span><span></span><span></span><span></span><span></span></div>
</body>
</html>
```